Creative - Appealing - Business Card Design Project

Looking for a Business card design (vector artwork) for an existing company called 'Copperfield Sound'. We operate in the entertainment industry specializing in audio system design and rental, however; we also deal with other sectors of the entertainment industry including lighting, video, staging and power system design and rental. We would like to see designs that don't focus too much on audio but include elements encompassing everything else.

Double sided business card, following our new colour scheme and logo, which is attached. The card would ideally be creative and eye catching to draw in new customers in the elegant event production market, such as weddings & corporate affairs.

Target Market(s)

High end corporate clients, wedding clients

Industry/Entity Type

Entertainment

Requirements
Must have
• Our contact details, these can be worded & listed however you think appropriate as part as the design

Business Name - Copperfield Sound
My Name - Benedict Thornbury
Web Address - www.copperfieldsound-example.com
Mobile Number - 07914 362 517
Office Number - 0330 411 7785
Email - ben@copperfieldsound-example.com

The name, email and mobile number would need to be able to be changed to my business partners also.

The font used on our logo is Sansation
Nice to have
• On one side maybe a word cloud involving the services in which we can provide; Lighting, Sound, Event Production, Staging, LED Uplighting, Projection Mapping, Wedding Hire

On the other side, all the important credentials of contact.
Should not have
• The design should not use any old style fonts (i.e Times New Roman, Gothic etc) or on the other side of the scale, any 'jokey' fonts (i.e. Comic Sans).

The font to be used is Sansation

```html
<!DOCTYPE html>
<html lang="en">
<head>
<meta charset="utf-8">
<title>Copperfield Sound – Business Card</title>
<link rel="stylesheet" href="https://fonts.googleapis.com/css2?family=Sansation:wght@400;700&display=swap">
<style>
  :root {
    --stage: #2f2f31;
    --brand-purple: #533a7f;
    --deep-purple: #4a2c68;
    --wave-start: #4e2d69;
    --wave-end: #8f66aa;
    --accent-line: #9a7ab8;
    --name-purple: #5a3a80;
    --ink: #2a2a2a;
    --muted-grey: #8a8a8c;
    --paper: #ffffff;
  }
  * { margin: 0; padding: 0; box-sizing: border-box; }
  html, body { width: 1200px; height: 900px; overflow: hidden; }
  body {
    background: var(--stage);
    font-family: "Sansation", "Trebuchet MS", sans-serif;
    position: relative;
  }
  .card {
    position: absolute;
    top: 306px;
    width: 520px;
    height: 288px;
    overflow: hidden;
  }
  .card--front { left: 65px; background: var(--brand-purple); }
  .card--back { left: 615px; background: var(--paper); }

  .front-name {
    position: absolute;
    inset: 0;
    display: flex;
    align-items: center;
    justify-content: center;
    gap: 16px;
    color: var(--paper);
    font-weight: 700;
    font-size: 38px;
    letter-spacing: 0.5px;
  }
  .front-name .mark {
    width: 22px; height: 22px; border-radius: 50%;
    background: var(--paper);
  }

  .back-name {
    position: absolute;
    left: 44px;
    top: 92px;
    width: 200px;
    color: var(--muted-grey);
    font-weight: 700;
    font-size: 27px;
    line-height: 1.1;
  }

  .contact {
    position: absolute;
    right: 30px;
    top: 28px;
    text-align: right;
    color: var(--ink);
  }
  .contact__person { color: var(--name-purple); font-weight: 700; font-size: 17px; }
  .contact__role { font-size: 14px; margin-top: 2px; }
  .contact__company { color: var(--name-purple); font-size: 16px; margin-top: 26px; }
  .contact__list { list-style: none; font-size: 13.5px; line-height: 17px; margin-top: 2px; }
  .contact__list li { display: flex; justify-content: flex-end; align-items: center; gap: 6px; }
  .contact__list svg { width: 11px; height: 11px; fill: var(--name-purple); flex: none; }

  .wave { position: absolute; left: 0; bottom: 0; width: 520px; height: 100px; }

  .services {
    position: absolute;
    right: 30px;
    bottom: 24px;
    text-align: right;
    color: var(--paper);
    font-size: 9.5px;
    line-height: 12px;
  }
</style>
</head>
<body>
  <section class="card card--front">
    <div class="front-name"><span class="mark"></span><span>COPPERFIELD SOUND</span></div>
  </section>

  <section class="card card--back">
    <div class="back-name">COPPERFIELD SOUND</div>

    <div class="contact">
      <div class="contact__person">Benedict Thornbury</div>
      <div class="contact__role">managing director</div>
      <div class="contact__company">Copperfield Sound</div>
      <ul class="contact__list">
        <li>07914 362 517
          <svg viewBox="0 0 12 12"><path d="M3 0h6a1 1 0 0 1 1 1v10a1 1 0 0 1-1 1H3a1 1 0 0 1-1-1V1a1 1 0 0 1 1-1zm.5 1.5v8h5v-8z"/></svg></li>
        <li>0330 411 7785
          <svg viewBox="0 0 12 12"><path d="M2.5 0.5l2 2.5-1.2 1.3c.7 1.6 2 2.9 3.4 3.6l1.3-1.2 2.5 2-1.3 2.3C5 10.8 1.2 7 .3 2z"/></svg></li>
        <li>ben@copperfieldsound-example.com
          <svg viewBox="0 0 12 12"><path d="M0 2h12v8H0z M0.8 2.6L6 6.6l5.2-4" fill="none" stroke="currentColor"/><path d="M0 2.5l6 4.3 6-4.3V10H0z"/></svg></li>
        <li>www.copperfieldsound-example.com
          <svg viewBox="0 0 12 12"><circle cx="6" cy="6" r="5.5"/><path d="M0.5 6h11M6 0.5v11M2 3h8M2 9h8" stroke="#fff" stroke-width="0.7" fill="none"/></svg></li>
      </ul>
    </div>

    <svg class="wave" viewBox="0 0 520 100" preserveAspectRatio="none" aria-hidden="true">
      <defs>
        <linearGradient id="bandFill" x1="0" x2="1" y1="0" y2="0">
          <stop offset="0" stop-color="var(--wave-start)"/>
          <stop offset="1" stop-color="var(--wave-end)"/>
        </linearGradient>
      </defs>
      <path d="M0 2 C120 30 260 36 520 6" fill="none" stroke="var(--accent-line)" stroke-width="4"/>
      <path d="M0 14 C130 40 270 42 520 14 L520 100 L0 100 Z" fill="url(#bandFill)"/>
    </svg>

    <div class="services">
      Lighting • Sound • Event Production • Staging<br>
      LED Uplighting • Projection Mapping • Wedding Hire
    </div>
  </section>
</body>
</html>
```